Business Card for new Overseas Property Buying Business

Hi

We need a new business card for our new business.

We are Faraway Nest Seekers. So we search locations on behalf of our clients to find them the ideal home.

These are mainly holiday homes in nice locations - but sometimes people are looking to relocate.

I am looking for a nice simple design - that has some class and professionalism about it. Taking inspiration from our logo.

Text wise I was thinking of maybe having something like. (THE FONT FOR THIS SHOULD BE LIKE THE WRITING IN THE ATTACHMENT WITH THE MAP ON IT)

1)
What does your dream house have (tick all that apply):
swimming pool x
private vineyard x
herb garden x
full sized football pitch x

2)
How to buy a home abroad:

Method 1:
1) Scour internet for suitable estate agents
2) Arrange hectic holiday timetable with multiple agents in multiple languages
3) Fly to destination to find property was not as it seemed
4) Feel frustrated and helpless
OR
Method 2:
Contact your expert home hunter (details overleaf) - and leave the hard work to them

The end result should give people confidence that they are dealing with a professional organisation - and feel like they can place their trust in them. I would want it to drive them to either contact us directly or visit the website.

Please include name (Gordon Marsh), position (founder), contact numbers x 2, email address, website (www.quillan-tarvo.com)

I look forward to seeing your entries.

```html
<!DOCTYPE html>
<html lang="en">
<head>
<meta charset="utf-8">
<title>Quillan &amp; Tarvo – Business Card</title>
<link rel="stylesheet" href="https://fonts.googleapis.com/css2?family=Tinos:wght@400;700&family=Open+Sans:wght@500;600&family=Caveat:wght@500&display=swap">
<style>
  :root {
    --backdrop: #d9ccf3;
    --paper-light: #f4f4f3;
    --paper-mid: #e4e4e2;
    --accent-orange: #f07348;
    --brand-grey: #6d6863;
    --rule-grey: #7b7672;
    --ink: #1e1e1e;
  }
  * { margin: 0; padding: 0; box-sizing: border-box; }
  html, body {
    width: 1200px; height: 800px; overflow: hidden;
    background: var(--backdrop);
  }
  .canvas { position: relative; width: 1200px; height: 800px; }

  .card {
    position: absolute; top: 251px;
    width: 521px; height: 298px;
    background: linear-gradient(135deg, var(--paper-light) 0%, var(--paper-mid) 55%, var(--paper-light) 100%);
    box-shadow: 0 2px 6px rgba(0,0,0,0.35);
    overflow: hidden;
  }
  .card--front { left: 52px; }
  .card--back { left: 627px; }

  /* Front */
  .front__url {
    position: absolute; left: 16px; top: 149px;
    transform: translate(-50%, -50%) rotate(-90deg);
    font: 600 15px/1 "Open Sans", sans-serif;
    letter-spacing: 0.5px; color: var(--ink); white-space: nowrap;
  }
  .front__rule-grey { position: absolute; left: 31px; top: 0; width: 4px; height: 100%; background: var(--rule-grey); }
  .front__rule-orange { position: absolute; left: 37px; top: 0; width: 3px; height: 100%; background: var(--accent-orange); }
  .front__mark {
    position: absolute; left: 218px; top: 22px;
    width: 110px; height: 110px; border-radius: 50%;
    background: var(--accent-orange);
  }
  .front__name {
    position: absolute; left: 40px; right: 0; top: 196px; text-align: center;
    font: 400 40px/1 "Tinos", serif; color: var(--brand-grey);
  }
  .front__division {
    position: absolute; left: 40px; right: 0; top: 240px; text-align: center;
    font: 400 16px/1 "Tinos", serif; letter-spacing: 0.6px; color: var(--brand-grey);
  }
  .front__tagline {
    position: absolute; left: 40px; right: 0; top: 260px; text-align: center;
    font: 500 26px/1 "Caveat", cursive; color: var(--accent-orange);
  }

  /* Back */
  .back__pitch {
    position: absolute; right: 12px; top: 10px; text-align: center;
    font: 500 27px/35px "Caveat", cursive; color: var(--accent-orange);
  }
  .back__mark {
    position: absolute; left: 33px; top: 20px;
    width: 46px; height: 46px; border-radius: 50%;
    background: var(--accent-orange);
  }
  .back__name { position: absolute; left: 14px; top: 92px; font: 400 19px/1 "Tinos", serif; color: var(--brand-grey); }
  .back__division { position: absolute; left: 16px; top: 113px; font: 400 8.5px/1 "Tinos", serif; letter-spacing: 0.3px; color: var(--brand-grey); }
  .back__url { position: absolute; left: 16px; top: 126px; font: 600 12.5px/1 "Open Sans", sans-serif; color: var(--ink); }

  .back__role { position: absolute; left: 2px; top: 180px; font: 400 19px/1 "Tinos", serif; color: var(--ink); }
  .back__role-rule { position: absolute; left: 0; top: 199px; width: 376px; height: 4px; background: var(--accent-orange); }
  .back__person { position: absolute; right: 8px; top: 187px; font: 700 22px/1 "Tinos", serif; color: var(--ink); }

  .back__phones { position: absolute; left: 10px; top: 248px; font: 500 15px/22px "Open Sans", sans-serif; color: var(--ink); }
  .back__email {
    position: absolute; right: 6px; top: 270px;
    display: flex; align-items: center; gap: 6px;
    font: 400 15px/1 "Tinos", serif; color: var(--ink);
  }
  .back__email svg { width: 20px; height: 20px; }
</style>
</head>
<body>
<main class="canvas">

  <section class="card card--front" aria-label="Card front">
    <div class="front__url">QUILLAN-TARVO.COM</div>
    <div class="front__rule-grey"></div>
    <div class="front__rule-orange"></div>
    <div class="front__mark"></div>
    <h1 class="front__name">Quillan &amp; Tarvo</h1>
    <p class="front__division">FARAWAY NEST SEEKERS</p>
    <p class="front__tagline">your expert home hunter</p>
  </section>

  <section class="card card--back" aria-label="Card back">
    <p class="back__pitch">Contact your expert home hunter<br>and leave the hard work to them</p>
    <div class="back__mark"></div>
    <p class="back__name">Quillan &amp; Tarvo</p>
    <p class="back__division">FARAWAY NEST SEEKERS</p>
    <p class="back__url">QUILLAN-TARVO.COM</p>

    <p class="back__role">Founder</p>
    <div class="back__role-rule"></div>
    <p class="back__person">Gordon Marsh</p>

    <p class="back__phones">Cell: 47120-381-904<br>Office: 47120- 829-316</p>
    <p class="back__email">
      <svg viewBox="0 0 20 20" aria-hidden="true">
        <rect x="2" y="5" width="16" height="11" rx="1" fill="#e9f2fb" stroke="#3a7fc4" stroke-width="1.3"/>
        <path d="M2.5 5.6 L10 11.5 L17.5 5.6" fill="none" stroke="#3a7fc4" stroke-width="1.3"/>
      </svg>
      gordon@quillan-tarvo.com
    </p>
  </section>

</main>
</body>
</html>
```